| Pairlocket | ||
| "Lanternmade Insurance" (this tagline includes the mathmatic "squared" symbol-see logo #161 winner) | ||
| Use fonts in logo. However, we may provide other direction on fonts for Address/Phone Numbers, etc. | ||
Cutting-Edge Modern Bright & Fun-filled |
| Dana R. Whitlock, MBA | ||
| Agency Principal | ||
| To Be Determined | ||
| TBD | ||
| dana@trypairlocket.com | ||
| www.trypairlocket.com | ||
1. We will need business cards for 2 people, Dana Whitlock (info provided above) and Morgan Whitlock...info as follows: Morgan P. Whitlock, MBA Agency Principal morgan@trypairlocket.com cell: 555.204.7316 2. Designer has provided final files to Mark Studio Hive. #161 was selected as Winner. This design has multiple components, please note. 3. Our logo style and design is somewhat "Retro" and cool, hip. We are in the insurance industry but definitely want to achieve a different "non-standard" look and feel. 4. Read Logo Brief for more information about the style of the two (twin brothers) Agency Principals. |
We are thinking that the "bottle cap" portion of our logo along with the "Pairlocket" portion would look good on the back of the business card. The bottle cap portion taking up most of the back of the card. Would like various options for the back. |
Download project material |
| pairlocket_17707.pdf |
| 1_17708.ai |
| Oak_Cellar_Depot_Business_Card_1_17709.jpg Pairlocket - Bus Card - example card design. We would like to see a style similar to this. |
| Brisk_Kettle_Business_Card_Example_17710.jpg Pairlocket - Bus Card - example card design. We would like to see a style similar to this. |

```html
<!DOCTYPE html>
<html lang="en">
<head>
<meta charset="utf-8">
<title>Pairlocket Stationery</title>
<link href="https://fonts.googleapis.com/css2?family=Montserrat:wght@400;600;800&display=swap" rel="stylesheet">
<style>
  :root{
    --green:#5c9e2e;
    --green-dark:#3f7d1f;
    --blue:#1f5a8c;
    --paper:#ffffff;
    --ink:#4a4a4a;
    --muted:#9a9a9a;
    --stage:#ece7df;
    --shadow:0 2px 5px rgba(0,0,0,.22);
  }
  *{box-sizing:border-box;margin:0;padding:0}
  html,body{width:1200px;height:382px;overflow:hidden}
  body{background:var(--stage);font-family:"Montserrat",Arial,sans-serif;color:var(--ink);position:relative}
  .piece{position:absolute;background:var(--paper);box-shadow:var(--shadow);overflow:hidden}
  .piece svg.deco{position:absolute;inset:0;width:100%;height:100%}
  .brand{font-weight:800;color:var(--green);letter-spacing:-.5px;line-height:1;position:relative}
  .brand.on-dark{color:#fff}
  .tagline{font-weight:600;color:var(--blue);text-transform:uppercase;letter-spacing:1px;line-height:1;position:relative}
  .caption{position:absolute;font-size:6px;color:var(--muted);text-align:center}
  .small{font-size:5px;line-height:1.5;position:relative;color:var(--ink)}
  .watermark{position:absolute;border-radius:50%;background:rgba(92,158,46,.08)}

  /* logo concept */
  .logo-concept{position:absolute;left:24px;top:34px;width:300px}
  .logo-concept .brand{font-size:40px}
  .logo-concept .tagline{font-size:9px;margin-top:6px;padding-left:4px;letter-spacing:2.4px}
  .logo-concept .caption{position:static;margin-top:8px;text-align:left;padding-left:100px}

  /* business cards */
  .card{width:144px;height:74px;padding:8px}
  .card-front-a{left:20px;top:168px}
  .card-back-a{left:170px;top:168px}
  .card-front-b{left:20px;top:262px;background:var(--green)}
  .card-back-b{left:170px;top:262px}
  .card .brand{font-size:14px}
  .card .tagline{font-size:3.5px;margin-top:2px}
  .card-front-a .brand,.card-front-b .brand{margin-top:20px;margin-left:26px}
  .card-front-a .tagline{margin-left:28px}
  .card-front-a .mark,.card-front-b .mark{position:absolute;left:10px;top:26px;width:16px;height:16px;border-radius:50%}
  .card-front-a .mark{background:var(--blue)}
  .card-front-b .mark{background:#fff}
  .card-back-a .brand,.card-back-b .brand{font-size:11px}
  .card-back-a .small,.card-back-b .small{margin-top:5px}
  .card-back-a .small b,.card-back-b .small b{color:var(--blue)}

  /* letterheads */
  .letterhead{width:188px;height:336px;top:24px;padding:14px}
  .letterhead-a{left:338px}
  .letterhead-b{left:544px}
  .letterhead .brand{font-size:13px}
  .letterhead .tagline{font-size:3.5px;margin-top:2px}
  .letterhead .contact{position:absolute;right:14px;top:16px;text-align:right;font-size:3.5px;line-height:1.6;color:var(--muted)}
  .letterhead .watermark{left:44px;top:112px;width:100px;height:100px}
  .letterhead .footer{position:absolute;left:40px;bottom:12px;font-size:3.5px;color:var(--muted)}

  /* envelopes */
  .envelope-back{left:758px;top:28px;width:430px;height:104px}
  .envelope-flap{left:758px;top:140px;width:430px;height:76px}
  .envelope-front{left:790px;top:222px;width:360px;height:76px}
  .envelope-small{left:758px;top:290px;width:258px;height:70px}
  .envelope .logo{position:absolute;left:50%;transform:translateX(-50%);text-align:center}
  .envelope .brand{font-size:10px}
  .envelope .tagline{font-size:3px;margin-top:2px}
  .envelope-back .logo{top:58px}
  .envelope-flap .logo{top:30px}
  .envelope-front .logo{top:30px}
  .envelope-small .logo{left:14px;top:10px;transform:none;text-align:left}
  .envelope-small .addr{position:absolute;left:14px;top:30px;font-size:3.5px;line-height:1.6;color:var(--muted)}

  .cap-cards{left:20px;top:346px;width:294px}
  .cap-lh-a{left:338px;top:364px;width:188px}
  .cap-lh-b{left:544px;top:364px;width:188px}
  .cap-env{left:1020px;top:354px;width:168px}
</style>
</head>
<body>

  <section class="logo-concept">
    <div class="brand">Pairlocket</div>
    <div class="tagline">Lanternmade Insurance</div>
    <div class="caption">Logo Concept</div>
  </section>

  <!-- business cards -->
  <article class="piece card card-front-a">
    <svg class="deco" viewBox="0 0 144 74" preserveAspectRatio="none" aria-hidden="true">
      <path d="M0 74 L0 58 Q40 70 144 52 L144 74 Z" fill="var(--green)"/>
      <path d="M0 60 Q40 68 144 50" stroke="var(--blue)" stroke-width="1.5" fill="none"/>
    </svg>
    <span class="mark"></span>
    <div class="brand">Pairlocket</div>
    <div class="tagline">Lanternmade Insurance</div>
  </article>

  <article class="piece card card-back-a">
    <svg class="deco" viewBox="0 0 144 74" preserveAspectRatio="none" aria-hidden="true">
      <path d="M120 0 Q112 40 144 74 L144 0 Z" fill="var(--green)"/>
      <path d="M116 0 Q108 40 138 74" stroke="var(--blue)" stroke-width="1.5" fill="none"/>
    </svg>
    <div class="brand">Pairlocket</div>
    <div class="small"><b>Dana R. Whitlock, MBA</b><br>Agency Principal<br>cell: 555.204.7316<br>dana@trypairlocket.com<br>www.trypairlocket.com</div>
  </article>

  <article class="piece card card-front-b">
    <svg class="deco" viewBox="0 0 144 74" preserveAspectRatio="none" aria-hidden="true">
      <path d="M0 74 L0 62 Q50 72 144 58 L144 74 Z" fill="var(--green-dark)"/>
    </svg>
    <span class="mark"></span>
    <div class="brand on-dark">Pairlocket</div>
  </article>

  <article class="piece card card-back-b">
    <svg class="deco" viewBox="0 0 144 74" preserveAspectRatio="none" aria-hidden="true">
      <path d="M120 0 Q112 40 144 74 L144 0 Z" fill="var(--green)"/>
      <path d="M116 0 Q108 40 138 74" stroke="var(--blue)" stroke-width="1.5" fill="none"/>
    </svg>
    <div class="brand">Pairlocket</div>
    <div class="small"><b>Morgan P. Whitlock, MBA</b><br>Agency Principal<br>cell: 555.204.7316<br>morgan@trypairlocket.com<br>www.trypairlocket.com</div>
  </article>
  <div class="caption cap-cards">Business Cards</div>

  <!-- letterheads -->
  <article class="piece letterhead letterhead-a">
    <svg class="deco" viewBox="0 0 188 336" preserveAspectRatio="none" aria-hidden="true">
      <path d="M150 0 Q176 30 188 70 L188 0 Z" fill="var(--blue)"/>
      <path d="M140 0 Q170 34 188 84" stroke="var(--green)" stroke-width="2" fill="none"/>
      <path d="M0 260 Q10 320 70 336 L0 336 Z" fill="var(--green)"/>
      <path d="M0 250 Q12 322 82 336" stroke="var(--blue)" stroke-width="2" fill="none"/>
    </svg>
    <div class="brand">Pairlocket</div>
    <div class="tagline">Lanternmade Insurance</div>
    <span class="watermark"></span>
    <div class="footer">www.trypairlocket.com · 555.204.7316</div>
  </article>

  <article class="piece letterhead letterhead-b">
    <svg class="deco" viewBox="0 0 188 336" preserveAspectRatio="none" aria-hidden="true">
      <path d="M0 270 Q20 326 188 312 L188 336 L0 336 Z" fill="var(--green)"/>
      <path d="M0 262 Q20 318 188 304" stroke="var(--blue)" stroke-width="2" fill="none"/>
    </svg>
    <div class="brand">Pairlocket</div>
    <div class="tagline">Lanternmade Insurance</div>
    <div class="contact">210 Harbor Lane, Suite 4<br>Pine Hollow, ST 00000<br>dana@trypairlocket.com</div>
    <span class="watermark"></span>
    <div class="footer">www.trypairlocket.com</div>
  </article>
  <div class="caption cap-lh-a">Letterhead Design 1</div>
  <div class="caption cap-lh-b">Letterhead Design 2</div>

  <!-- envelopes -->
  <article class="piece envelope envelope-back">
    <svg class="deco" viewBox="0 0 430 104" preserveAspectRatio="none" aria-hidden="true">
      <path d="M0 0 L430 0 L430 30 Q215 70 0 30 Z" fill="var(--blue)"/>
      <path d="M0 34 Q215 74 430 34" stroke="var(--green)" stroke-width="2" fill="none"/>
    </svg>
    <div class="logo"><div class="brand">Pairlocket</div><div class="tagline">Lanternmade Insurance</div></div>
  </article>

  <article class="piece envelope envelope-flap">
    <svg class="deco" viewBox="0 0 430 76" preserveAspectRatio="none" aria-hidden="true">
      <path d="M0 0 L430 0 L430 8 Q215 40 0 8 Z" fill="var(--green)"/>
    </svg>
    <div class="logo"><div class="brand">Pairlocket</div><div class="tagline">Lanternmade Insurance</div></div>
  </article>

  <article class="piece envelope envelope-front">
    <svg class="deco" viewBox="0 0 360 76" preserveAspectRatio="none" aria-hidden="true">
      <path d="M0 0 L360 0 L360 6 Q180 30 0 6 Z" fill="var(--green)"/>
    </svg>
    <div class="logo"><div class="brand">Pairlocket</div><div class="tagline">Lanternmade Insurance</div></div>
  </article>

  <article class="piece envelope envelope-small">
    <svg class="deco" viewBox="0 0 258 70" preserveAspectRatio="none" aria-hidden="true">
      <path d="M0 54 Q40 68 258 62 L258 70 L0 70 Z" fill="var(--green)"/>
      <path d="M0 50 Q40 64 258 58" stroke="var(--blue)" stroke-width="1.5" fill="none"/>
    </svg>
    <div class="logo"><div class="brand">Pairlocket</div><div class="tagline">Lanternmade Insurance</div></div>
    <div class="addr">210 Harbor Lane, Suite 4<br>Pine Hollow, ST 00000</div>
  </article>
  <div class="caption cap-env">Envelope Design</div>

</body>
</html>
```